Business card with logo and words.

Colours: aqua and white (but open to suggestions).
Double sided card ok.
Need to convey competence, calmness, listening skills
Words:
Quiet Harbour Care Planning
Rhoda Pemberton
RN, RM, MVRNB, Grad Dip Gr & Pall Care Couns, Grad Cert Pall Care in Aged Care
quietharbourcp@fernmail.example

```html
<!DOCTYPE html>
<html lang="en">
<head>
<meta charset="utf-8">
<title>Quiet Harbour Care Planning – Business Card</title>
<link rel="stylesheet" href="https://fonts.googleapis.com/css2?family=Jost:wght@300;400;500&display=swap">
<style>
  :root {
    --paper: #ffffff;
    --aqua: #2aa9c2;
    --ocean: #1674b6;
    --ink-blue: #1f6fae;
  }
  html, body {
    margin: 0;
    padding: 0;
    width: 1200px;
    height: 734px;
    overflow: hidden;
    background: var(--paper);
  }
  .card {
    position: relative;
    width: 1200px;
    height: 734px;
    background: var(--paper);
    font-family: "Jost", "Futura", sans-serif;
  }
  .brand-name {
    position: absolute;
    left: 37px;
    top: 34px;
    margin: 0;
    font-size: 26px;
    font-weight: 400;
    line-height: 1;
    color: var(--aqua);
  }
  .brand-dot {
    position: absolute;
    left: 164px;
    top: 76px;
    width: 128px;
    height: 128px;
  }
  .person {
    position: absolute;
    left: 598px;
    top: 196px;
  }
  .person-name {
    margin: 0;
    font-size: 72px;
    font-weight: 500;
    line-height: 1;
    color: var(--ocean);
    letter-spacing: 0.2px;
  }
  .credentials {
    margin: 22px 0 0 10px;
    font-size: 17px;
    font-weight: 400;
    line-height: 24px;
    color: var(--ocean);
    text-transform: uppercase;
    letter-spacing: 0.2px;
  }
  .contact {
    position: absolute;
    left: 41px;
    top: 482px;
    margin: 0;
    display: grid;
    grid-template-columns: 219px auto;
    row-gap: 12px;
    font-size: 47px;
    line-height: 52px;
    color: var(--ink-blue);
  }
  .contact dt { margin: 0; font-weight: 400; }
  .contact dd { margin: 0; font-weight: 300; }
</style>
</head>
<body>
  <main class="card">
    <p class="brand-name">Quiet Harbour Care Planning</p>
    <svg class="brand-dot" viewBox="0 0 128 128" aria-hidden="true">
      <circle cx="64" cy="64" r="64" fill="var(--aqua)"/>
    </svg>

    <section class="person">
      <h1 class="person-name">Rhoda Pemberton</h1>
      <p class="credentials">RN, RM, MVRNB, Grad Dip Gr &amp; Pall Care Couns,<br>Grad Cert Pall Care in Aged Care</p>
    </section>

    <dl class="contact">
      <dt>Mobile:</dt><dd>xxxx xxx xxx</dd>
      <dt>Email:</dt><dd>quietharbourcp@fernmail.example</dd>
      <dt>Web:</dt><dd>www.xxxxxx.xxx.xx</dd>
    </dl>
  </main>
</body>
</html>
```